Course Graduation Certificate

This project is not for a flyer but instead for the creation of a course graduation certificate. The final certificate needs to include the Marlowe Summit Aviation Academy logo and the text stating as follows:
Certifies that ___________________________ has satisfactorily completed the course of _______________________________ on ________________________________
I would also like to include some type of gold seal of completion as well as a place to sign my name and credentials at the bottom of the certificate
I have included the Marlowe Summit Aviation Academy logo as well as three other certificate examples for you to work from.
Target Market(s)
Students completing a certification course and receiving a certificate
Look and feel

```html
<!DOCTYPE html>
<html lang="en">
<head>
<meta charset="utf-8">
<title>Course Graduation Certificate – Marlowe Summit Aviation Academy</title>
<link rel="stylesheet" href="https://fonts.googleapis.com/css2?family=Montserrat:wght@400;500;700&family=Playfair+Display:wght@700;800&display=swap">
<style>
  :root {
    --navy: #0b3a6e;
    --blue: #0d4a8c;
    --blue-light: #2f6aa8;
    --gold: #b8892a;
    --gold-light: #f1d77a;
    --gold-dark: #8a6414;
    --ink: #222222;
    --paper: #ffffff;
    --paper-shade: #f3f3f1;
  }
  * { box-sizing: border-box; margin: 0; padding: 0; }
  html, body { width: 1200px; height: 857px; overflow: hidden; background: var(--paper); }
  .certificate {
    position: relative;
    width: 1200px; height: 857px;
    overflow: hidden;
    background: radial-gradient(ellipse at 60% 50%, var(--paper) 0%, var(--paper-shade) 100%);
    font-family: "Montserrat", sans-serif;
    color: var(--ink);
  }
  .frame-art { position: absolute; inset: 0; }
  .plane-art {
    position: absolute; left: 300px; top: 95px; width: 240px; height: 100px;
    background: radial-gradient(ellipse at 50% 50%, var(--gold) 0%, rgba(184,137,42,0.55) 45%, rgba(184,137,42,0) 72%);
  }
  .title {
    position: absolute; left: 0; right: 0; top: 188px;
    padding-left: 0;
    text-align: center;
    font-family: "Playfair Display", serif;
    font-weight: 800;
    font-size: 116px;
    line-height: 1;
    letter-spacing: -1px;
    background: linear-gradient(180deg, var(--gold-light) 0%, var(--gold) 55%, var(--gold-dark) 100%);
    -webkit-background-clip: text; background-clip: text;
    color: transparent;
    transform: translateX(-2px);
  }
  .presented {
    position: absolute; left: 0; right: 0; top: 316px;
    text-align: center; font-size: 14px; letter-spacing: 0.3px; text-transform: uppercase;
  }
  .fill-row {
    position: absolute; display: flex; align-items: flex-end;
    font-size: 18px; font-weight: 400;
  }
  .fill-line {
    display: inline-block; height: 3px; margin-left: 6px; margin-bottom: 5px;
    background: linear-gradient(90deg, var(--gold-dark), var(--gold-light) 50%, var(--gold-dark));
  }
  .row-name { left: 300px; top: 406px; }
  .row-name .fill-line { width: 458px; }
  .row-course { left: 166px; top: 493px; }
  .row-course .fill-line { width: 464px; margin-left: 12px; }
  .row-date { left: 356px; top: 580px; }
  .row-date .fill-line { width: 460px; margin-left: 6px; }
  .signature {
    position: absolute; top: 702px; text-align: center;
  }
  .signature-line {
    height: 3px; width: 100%;
    background: linear-gradient(90deg, var(--gold-dark), var(--gold-light) 50%, var(--gold-dark));
  }
  .signature-label {
    margin-top: 6px;
    font-family: "Playfair Display", serif; font-weight: 700;
    font-size: 34px; color: var(--navy); line-height: 1;
  }
  .signature-role { margin-top: 8px; font-size: 14px; }
  .sign-date { left: 288px; width: 243px; }
  .sign-director { left: 588px; width: 400px; }
  .sign-director .signature-line { width: 347px; }
  .sign-director .signature-label, .sign-director .signature-role { width: 400px; margin-left: 0; text-align: center; transform: translateX(0); }
  .brand-pennant { position: absolute; left: 872px; top: 0; width: 312px; height: 228px; }
  .brand-name {
    position: absolute; left: 892px; top: 96px; width: 272px;
    text-align: center;
    font-family: "Montserrat", sans-serif; font-weight: 700;
    font-size: 19px; line-height: 1.25; color: var(--gold-light);
    text-transform: uppercase; letter-spacing: 1px;
  }
  .seal { position: absolute; left: 926px; top: 588px; width: 180px; height: 180px; }
</style>
</head>
<body>
<main class="certificate">

  <svg class="frame-art" width="1200" height="857" viewBox="0 0 1200 857" aria-hidden="true">
    <defs>
      <linearGradient id="goldStroke" x1="0" y1="0" x2="0" y2="1">
        <stop offset="0" stop-color="#f1d77a"/>
        <stop offset="0.5" stop-color="#b8892a"/>
        <stop offset="1" stop-color="#f1d77a"/>
      </linearGradient>
      <linearGradient id="blueFill" x1="0" y1="0" x2="1" y2="1">
        <stop offset="0" stop-color="#0b3a6e"/>
        <stop offset="1" stop-color="#0d4a8c"/>
      </linearGradient>
      <linearGradient id="swoosh" x1="1" y1="0" x2="0" y2="1">
        <stop offset="0" stop-color="#8a6414"/>
        <stop offset="0.5" stop-color="#f1d77a"/>
        <stop offset="1" stop-color="#b8892a"/>
      </linearGradient>
    </defs>
    <!-- left blue band -->
    <path d="M0 0 H298 C170 120 95 280 100 450 C105 620 200 760 345 857 H0 Z" fill="url(#blueFill)"/>
    <path d="M0 0 H200 C95 140 40 300 45 460 C50 630 120 760 220 857 H0 Z" fill="#0b3a6e"/>
    <path d="M240 0 C130 130 70 290 72 455 C75 630 165 770 290 857" fill="none" stroke="#2f6aa8" stroke-width="10" opacity="0.7"/>
    <!-- gold rim -->
    <path d="M298 0 C170 120 95 280 100 450 C105 620 200 760 345 857" fill="none" stroke="url(#goldStroke)" stroke-width="12"/>
    <path d="M0 655 C90 640 180 700 250 857" fill="none" stroke="url(#goldStroke)" stroke-width="8" opacity="0.9"/>
    <!-- swoosh trailing from the plane -->
    <path d="M0 320 C120 270 230 215 335 178 C230 230 120 300 0 360 Z" fill="url(#swoosh)"/>
  </svg>

  <div class="plane-art" role="img" aria-label="Gold airplane silhouette climbing to the upper right"></div>

  <svg class="brand-pennant" viewBox="0 0 312 228" aria-hidden="true">
    <defs>
      <linearGradient id="pennantFill" x1="0" y1="0" x2="0" y2="1">
        <stop offset="0" stop-color="#0b3a6e"/>
        <stop offset="1" stop-color="#1158a3"/>
      </linearGradient>
    </defs>
    <path d="M2 0 V172 L156 224 L310 172 V0 Z" fill="url(#pennantFill)" stroke="#b8892a" stroke-width="4"/>
  </svg>
  <div class="brand-name">Marlowe Summit<br>Aviation Academy</div>

  <h1 class="title">Certificate</h1>
  <p class="presented">This certificate is proudly presented to:</p>

  <p class="fill-row row-name">Certifies that<span class="fill-line"></span></p>
  <p class="fill-row row-course">has satisfactorily completed the course of<span class="fill-line"></span></p>
  <p class="fill-row row-date">on<span class="fill-line"></span></p>

  <div class="signature sign-date">
    <div class="signature-line"></div>
    <div class="signature-label">Date</div>
  </div>
  <div class="signature sign-director">
    <div class="signature-line"></div>
    <div class="signature-label">Your Name</div>
    <div class="signature-role">Director and General Manager.</div>
  </div>

  <svg class="seal" viewBox="0 0 180 180" role="img" aria-label="Gold seal of completion">
    <defs>
      <radialGradient id="sealGold" cx="0.4" cy="0.35" r="0.7">
        <stop offset="0" stop-color="#f1d77a"/>
        <stop offset="1" stop-color="#8a6414"/>
      </radialGradient>
    </defs>
    <circle cx="90" cy="90" r="88" fill="url(#sealGold)"/>
    <circle cx="90" cy="90" r="76" fill="#0b3a6e"/>
    <circle cx="90" cy="90" r="56" fill="none" stroke="#b8892a" stroke-width="2"/>
  </svg>

</main>
</body>
</html>
```